Design some Business Cards for Consultant

Most of my work is in financial & analytical consulting for microfinance and low-income housing finance, mainly in developing countries (Asia, Africa, Latin America). You can see samples of my published work here: tomasvelkind.com (main page is the blog; navigate to /papers for other published work).

Looking for a clean, no-nonsense design with limited text (name, city, website, email, skype & phone). Single-sided. Would like to print on recycled paper stock, so consider this in the design. If you can work with a (reasonably priced) online printer that ships to Belgium at reasonable cost, would pay extra for the reference and selection of appropriate paper stock, but this isn't required.

Don't hesitate if you need additional info for your design. Will provide detailed text to the contest winner.

```html
<!DOCTYPE html>
<html lang="en">
<head>
<meta charset="utf-8">
<title>Tomas Velkind — Business Card</title>
<link rel="stylesheet" href="https://fonts.googleapis.com/css2?family=Open+Sans:wght@400;600;700;800&display=swap">
<style>
  :root {
    --page-bg: #e9e7e3;
    --card-white: #ffffff;
    --navy: #0f3553;
    --navy-text: #123a57;
    --accent-red: #d3281b;
    --divider: #1c4260;
  }
  * { box-sizing: border-box; margin: 0; padding: 0; }
  html, body {
    width: 1200px; height: 1016px; overflow: hidden;
    background: var(--page-bg);
    font-family: "Open Sans", Arial, sans-serif;
  }
  .business-card {
    position: absolute; left: 100px; top: 222px;
    width: 1000px; height: 572px;
    background: var(--card-white);
    box-shadow: 0 14px 36px rgba(0,0,0,0.18);
    overflow: hidden;
  }
  .brand-mark {
    position: absolute; left: 70px; top: 170px;
    width: 240px; display: flex; align-items: center; gap: 12px;
    color: var(--navy); font-weight: 700; font-size: 30px; letter-spacing: 3px;
  }
  .brand-mark .brand-dot {
    width: 22px; height: 22px; border-radius: 50%; background: var(--navy);
    flex: none;
  }
  .divider {
    position: absolute; left: 360px; top: 80px;
    width: 2px; height: 300px; background: var(--divider);
  }
  .identity {
    position: absolute; right: 56px; top: 70px; text-align: right;
  }
  .identity .person-name {
    color: var(--accent-red); font-weight: 700; font-size: 44px;
    letter-spacing: 5px; line-height: 1;
  }
  .identity .job-title {
    color: var(--navy-text); font-weight: 700; font-size: 14px;
    letter-spacing: 2.5px; margin-top: 8px;
  }
  .contact-list {
    position: absolute; left: 410px; top: 178px; list-style: none;
  }
  .contact-list li {
    display: flex; align-items: center; gap: 14px;
    color: var(--navy-text); font-size: 17px; font-weight: 600;
    letter-spacing: 2px; height: 36px;
  }
  .contact-list .icon { width: 20px; height: 20px; flex: none; }
  .skype-dot {
    width: 20px; height: 20px; border-radius: 50%; background: var(--accent-red); flex: none;
  }
  .website {
    position: absolute; left: 410px; top: 316px;
    color: var(--navy-text); font-size: 26px; letter-spacing: 4px; font-weight: 400;
  }
  .website strong { font-weight: 800; }
  .address-band {
    position: absolute; left: 0; bottom: 0; width: 100%; height: 150px;
    background: var(--navy);
    display: flex; align-items: center; padding-left: 50px;
    color: #ffffff; font-size: 22px; font-weight: 600; letter-spacing: 3px;
  }
</style>
</head>
<body>
  <div class="business-card">
    <div class="brand-mark"><span class="brand-dot"></span><span>VELKIND</span></div>
    <div class="divider"></div>

    <div class="identity">
      <div class="person-name">TOMAS VELKIND</div>
      <div class="job-title">MICROFINANCE CONSULTANT</div>
    </div>

    <ul class="contact-list">
      <li>
        <svg class="icon" viewBox="0 0 24 24" aria-hidden="true"><path fill="#d3281b" d="M6.6 10.8a15.1 15.1 0 0 0 6.6 6.6l2.2-2.2a1 1 0 0 1 1-.25 11.4 11.4 0 0 0 3.6.57 1 1 0 0 1 1 1V20a1 1 0 0 1-1 1A17 17 0 0 1 3 4a1 1 0 0 1 1-1h3.5a1 1 0 0 1 1 1c0 1.25.2 2.45.57 3.57a1 1 0 0 1-.25 1z"/></svg>
        <span>+32 470 218 45</span>
      </li>
      <li>
        <svg class="icon" viewBox="0 0 24 24" aria-hidden="true"><rect x="2" y="5" width="20" height="14" rx="1.5" fill="#d3281b"/><path d="M3 6.5l9 6.5 9-6.5" fill="none" stroke="#fff" stroke-width="1.6"/></svg>
        <span>TOMAS@TOMASVELKIND.COM</span>
      </li>
      <li>
        <span class="skype-dot" aria-hidden="true"></span>
        <span>TOMASVELKIND</span>
      </li>
    </ul>

    <div class="website">WWW.<strong>TOMASVELKIND</strong>.COM</div>

    <div class="address-band">1420 HARBOR LANE HEIGHTS, K2B 7R4 VELMONT</div>
  </div>
</body>
</html>
```